Dog care service needs advertising poster

Our company is Paw Haven. We provide care for dogs while their owners are away, either through home visits or a holiday stay in the homes of carefully selected minders. Our existing website & Facebook cover should provide all the colour cues for a poster - namely blues, blondes and grey. We have an existing logo (provided). We can feature the same imagery from our website as I have purchased the rights to the stock images.

www.pawhavenexample.com.au
www.facebook.com/pawhavenexampleau

This brief is for design of a poster that can be placed in vet surgeries, groomers, on community noticeboards. It should be scalable to print in three sizes, A5, A4 & A3.

We wish to clearly communicate our three areas of service "dog minding, home visits, dog walking".

We would like to have the files ready for upload to Printora (or similar) for immediate printing.

Target Market(s)

Dog owners who love their dogs like family.

Industry/Entity Type

Advertising

Font styles to use
Sans Serif

Colors
33a6d7
3276b5

Requirements
Must have
• Logo
• www.pawhavenexample.com.au
• Telephone number
• Three services - Dog Minding, Home Visits, Dog Walking
Nice to have
• use of our existing stock photography to highlight the three areas of service - Dog minding, home visits, dog walking. Existing colour palette - blues, blondes and grey.
• Text that can be used:
• Western Sydney’s complete dog care service.
• Dog Minding - Your dog stays in the home of one of our carefully selected minders.Treated like part of the family, they enjoy all the creature comforts they are used to.
• Home Visits - We visit your dog at your home for feeding, walking and playtime. Short of long visits available.
• Dog Walking - If you can't walk your dog for any reason we are here to help. 1/2 hour or hourly walks available.
• Contact us today for a tailored package to meet your needs.
Should not have
• Any additional illustrations beyond the logo.

```html
<!DOCTYPE html>
<html lang="en">
<head>
<meta charset="utf-8">
<title>Paw Haven Poster</title>
<link href="https://fonts.googleapis.com/css2?family=Lato:ital,wght@0,400;0,700;0,900;1,900&display=swap" rel="stylesheet">
<style>
  :root {
    --backdrop: #e9e6e2;
    --paper: #ffffff;
    --ink-grey: #3f4a56;
    --sky-blue: #2199d6;
    --teal-blue: #1f7fb0;
    --navy: #1f3572;
    --brand-blue: #33a6d7;
    --photo-light: #f4ece0;
    --photo-mid: #e6d3b8;
    --photo-deep: #cdb592;
    --white: #ffffff;
  }
  * { margin: 0; padding: 0; box-sizing: border-box; }
  html, body { width: 1200px; height: 926px; overflow: hidden; }
  body { background: var(--backdrop); font-family: "Lato", Arial, sans-serif; position: relative; }

  .poster {
    position: absolute; left: 46px; top: 40px; width: 1102px; height: 848px;
    background: var(--paper); overflow: hidden;
    box-shadow: 0 4px 14px rgba(0,0,0,0.25);
  }
  .hero-photo {
    position: absolute; left: 320px; top: 0; width: 782px; height: 610px;
    background: radial-gradient(ellipse at 55% 50%, var(--photo-mid) 0%, var(--photo-light) 45%, rgba(255,255,255,0) 72%),
                radial-gradient(ellipse at 60% 75%, var(--photo-deep) 0%, rgba(205,181,146,0) 55%);
  }
  .swoosh { position: absolute; left: 0; top: 0; width: 1102px; height: 848px; }

  .brand { position: absolute; left: 34px; top: 58px; display: flex; align-items: center; gap: 18px; }
  .brand-dot { width: 86px; height: 86px; border-radius: 50%; background: var(--ink-grey); }
  .brand-name { font-weight: 700; font-size: 50px; color: var(--ink-grey); letter-spacing: -0.5px; }

  .tagline {
    position: absolute; left: 32px; top: 208px;
    font-size: 34px; line-height: 46px; font-weight: 400; color: var(--ink-grey);
  }
  .phone {
    position: absolute; left: 34px; top: 330px; display: flex; align-items: center; gap: 14px;
    font-size: 31px; font-weight: 700; color: var(--ink-grey);
  }
  .phone svg { width: 46px; height: 46px; }

  .services { position: absolute; left: 0; top: 628px; width: 760px; }
  .service {
    position: absolute; display: flex; align-items: center; gap: 8px;
    font-weight: 900; font-style: italic; font-size: 32px; color: var(--white);
    text-shadow: 2px 2px 3px rgba(0,0,0,0.55); white-space: nowrap;
  }
  .service::before {
    content: ""; width: 34px; height: 34px; border-radius: 50%;
    border: 4px solid var(--white); box-shadow: 1px 1px 3px rgba(0,0,0,0.4);
  }
  .service-minding { left: 104px; top: 0; }
  .service-visits { left: 400px; top: 0; }
  .service-walking { left: 236px; top: 70px; }

  .divider { position: absolute; left: 50px; top: 773px; width: 686px; height: 1px; background: rgba(255,255,255,0.85); }
  .website {
    position: absolute; left: 134px; top: 796px; display: flex; align-items: center; gap: 14px;
    font-size: 30px; font-weight: 700; color: var(--white);
  }
  .website svg { width: 26px; height: 26px; }
</style>
</head>
<body>
  <main class="poster">
    <div class="hero-photo" role="img" aria-label="Stock photo of a smiling woman hugging three cream golden retriever puppies"></div>

    <svg class="swoosh" viewBox="0 0 1102 848" aria-hidden="true">
      <path d="M0,440 Q280,560 720,612 Q930,630 1102,600 L1102,848 L0,848 Z" fill="var(--teal-blue)"/>
      <path d="M0,500 Q330,610 720,620 Q930,622 1030,590 L1102,848 L0,848 Z" fill="var(--sky-blue)"/>
      <path d="M680,848 Q940,760 1030,592 L1102,466 L1102,848 Z" fill="var(--navy)"/>
    </svg>

    <header class="brand">
      <span class="brand-dot"></span>
      <span class="brand-name">Paw Haven</span>
    </header>

    <p class="tagline">Western Sydney’s complete<br>Dog care service</p>

    <p class="phone">
      <svg viewBox="0 0 46 46" aria-hidden="true">
        <circle cx="23" cy="23" r="20" fill="none" stroke="var(--ink-grey)" stroke-width="3"/>
        <path d="M16,12 L20,12 L22,18 L19,20 Q21,25 26,27 L28,24 L34,26 L34,30 Q33,34 29,34 Q14,32 12,17 Q12,12 16,12 Z" fill="var(--ink-grey)"/>
      </svg>
      0400 555 019
    </p>

    <ul class="services">
      <li class="service service-minding">Dog Minding</li>
      <li class="service service-visits">Home Visits</li>
      <li class="service service-walking">Dog Walking</li>
    </ul>

    <div class="divider"></div>

    <p class="website">
      <svg viewBox="0 0 26 26" aria-hidden="true" fill="none" stroke="var(--white)" stroke-width="1.8">
        <circle cx="13" cy="13" r="11"/>
        <ellipse cx="13" cy="13" rx="5" ry="11"/>
        <line x1="2" y1="13" x2="24" y2="13"/>
        <path d="M4,7 H22 M4,19 H22"/>
      </svg>
      www.pawhavenexample.com.au
    </p>
  </main>
</body>
</html>
```